Kelvara Constructions Business card and Logo

We are a building company that would like our current logo design copied with the "Kelvara Constructions" lines thicker.
We would also like our business cards copied with some minor copy changes. I have attached images of our logo and business cards.
We would like a standard size business card in landscape format rather than portrait.
On the back of the business card we would like a name added above the mobile number - "Teodor Marsk"
Can I please get high res file of the logo and business cards at completion of redesign?

```html
<!DOCTYPE html>
<html lang="en">
<head>
<meta charset="utf-8">
<title>Kelvara Constructions – Business Card</title>
<link rel="stylesheet" href="https://fonts.googleapis.com/css2?family=Montserrat:wght@400;500;600&display=swap">
<style>
  :root {
    --page-bg: #ecebe8;
    --card-white: #ffffff;
    --card-blue: #1aa9e6;
    --brand-blue: #1aa9e6;
    --text-light: #ffffff;
    --card-shadow: 0 14px 30px rgba(0, 0, 0, 0.18);
  }
  * { box-sizing: border-box; margin: 0; padding: 0; }
  html, body {
    width: 1200px;
    height: 870px;
    overflow: hidden;
    background: var(--page-bg);
    font-family: "Montserrat", sans-serif;
  }
  .canvas {
    position: relative;
    width: 1200px;
    height: 870px;
    display: flex;
    align-items: center;
    justify-content: center;
    gap: 60px;
  }
  .card {
    width: 525px;
    height: 300px;
    border-radius: 4px;
    box-shadow: var(--card-shadow);
    position: relative;
    overflow: hidden;
  }
  .card--front {
    background: var(--card-white);
    display: flex;
    align-items: center;
    justify-content: center;
  }
  .brand {
    display: flex;
    align-items: center;
    gap: 14px;
  }
  .brand__dot {
    width: 18px;
    height: 18px;
    border-radius: 50%;
    background: var(--brand-blue);
  }
  .brand__name {
    font-size: 30px;
    font-weight: 600;
    color: var(--brand-blue);
    letter-spacing: 0.5px;
  }
  .card--back {
    background: var(--card-blue);
    color: var(--text-light);
    padding: 38px 40px;
    display: flex;
    justify-content: space-between;
  }
  .person__name {
    font-size: 20px;
    font-weight: 500;
    letter-spacing: 2px;
    text-transform: uppercase;
  }
  .person__role {
    font-size: 13px;
    margin-top: 4px;
    letter-spacing: 0.5px;
  }
  .contact {
    align-self: flex-end;
    list-style: none;
    font-size: 12px;
    display: flex;
    flex-direction: column;
    gap: 9px;
    text-align: right;
  }
  .contact__item {
    display: flex;
    align-items: center;
    justify-content: flex-end;
    gap: 10px;
  }
  .contact__item--address { margin-bottom: 8px; line-height: 1.45; }
  .contact__icon { width: 13px; height: 13px; flex: none; }
</style>
</head>
<body>
<main class="canvas">
  <section class="card card--front" aria-label="Card front">
    <div class="brand">
      <span class="brand__dot"></span>
      <span class="brand__name">Kelvara Constructions</span>
    </div>
  </section>

  <section class="card card--back" aria-label="Card back">
    <div class="person">
      <p class="person__name">Teodor Marsk</p>
      <p class="person__role">Managing Director</p>
    </div>
    <ul class="contact">
      <li class="contact__item contact__item--address">Level 4, 27 Harbour Row<br>Wexmoor</li>
      <li class="contact__item">021 480 3175
        <svg class="contact__icon" viewBox="0 0 16 16" fill="none" stroke="#fff" stroke-width="1.6"><path d="M4 1.5h3l1 3.5-2 1.2a8 8 0 0 0 3.8 3.8L11 8l3.5 1v3c0 1-1 2-2 2A11 11 0 0 1 2 3.5c0-1 1-2 2-2z"/></svg>
      </li>
      <li class="contact__item">021 480 3176
        <svg class="contact__icon" viewBox="0 0 16 16" fill="none" stroke="#fff" stroke-width="1.6"><rect x="4" y="1" width="8" height="14" rx="1.5"/><line x1="7" y1="12.5" x2="9" y2="12.5"/></svg>
      </li>
      <li class="contact__item">021 480 3177
        <svg class="contact__icon" viewBox="0 0 16 16" fill="#fff"><rect x="1" y="6" width="14" height="7" rx="1"/><rect x="4" y="1.5" width="8" height="4"/><rect x="4" y="11" width="8" height="4" fill="#fff" stroke="#1aa9e6"/></svg>
      </li>
      <li class="contact__item">office@kelvarabuild.com
        <svg class="contact__icon" viewBox="0 0 16 16" fill="none" stroke="#fff" stroke-width="1.5"><rect x="1" y="3" width="14" height="10" rx="1"/><path d="M1 3l7 6 7-6"/></svg>
      </li>
      <li class="contact__item">www.kelvarabuild.com
        <svg class="contact__icon" viewBox="0 0 16 16" fill="none" stroke="#fff" stroke-width="1.3"><circle cx="8" cy="8" r="6.5"/><ellipse cx="8" cy="8" rx="3" ry="6.5"/><line x1="1.5" y1="8" x2="14.5" y2="8"/></svg>
      </li>
    </ul>
  </section>
</main>
</body>
</html>
```